Brindle Advisory Business Card Design

Business card for business consulting company, using attached logo. We do financial and strategic consulting, and want a clean, professional image with a bit of fun. Our logo is a flat whale tail, which symbolizes the Orca whale, a highly collaborative, group based animal that is very successful in navigating the ocean, protecting the herd, and hunting. We like the logo that is blue and gray on white one one side, but would be open to a blue card with white lettering on the other side... or whatever you'd suggest
Updates
Hi all - I have had the logo modified to take the shadowing off the tail. I will post it on the brief... under a file name called updated logo. thank you Added Saturday, April 25, 2015
Target Market(s)
Small to medium sized businesses ($10M to $500M in revenue per year), financial and sales executives, general managers, attorneys and CPAs
Industry/Entity Type
Financial
Contact Information for Business Card
Want company name, contact info - name, title, telephone, email, website, linkedin, twitter and Facebook. No physical address yet.
Requirements
Must have
- contemporary design, bold, strong, confident but with a bit of fun. prominently feature the logo and the whale tail icon
Nice to have
- unique touches that would differentiate us from a regular card... for example, logo and writing all on front on white background, but on back - logo in white on a blue background
- open to idea of different shapes of card than standard... but not sure
Should not have
- ?

```html
<!DOCTYPE html>
<html lang="en">
<head>
<meta charset="utf-8">
<title>Brindle Advisory – Business Card</title>
<link href="https://fonts.googleapis.com/css2?family=Open+Sans:ital,wght@0,300;0,400;0,600;0,700;1,400&display=swap" rel="stylesheet">
<style>
  :root {
    --page: #e9e6e1;
    --white: #ffffff;
    --paper-shade: #eef0f3;
    --navy: #1f4f94;
    --blue: #0d57a6;
    --blue-deep: #0a3f80;
    --blue-light: #2f7fc4;
    --cyan: #7cc2e6;
    --grey-text: #8f949b;
    --grey-mark: #c9cbd3;
    --name-blue: #2c6fb4;
  }
  * { box-sizing: border-box; margin: 0; padding: 0; }
  html, body {
    width: 1200px; height: 1023px; overflow: hidden;
    background: var(--page);
    font-family: "Open Sans", Arial, sans-serif;
  }
  .sheet { position: relative; width: 1200px; height: 1023px; }

  .card {
    position: absolute; left: 250px; width: 700px; height: 400px;
    border-radius: 4px; overflow: hidden;
    box-shadow: 0 6px 18px rgba(0,0,0,.18);
  }

  /* front */
  .card--front {
    top: 60px;
    background: linear-gradient(180deg, var(--white) 0%, var(--paper-shade) 100%);
  }
  .front__mark-bg {
    position: absolute; right: 40px; top: 36px;
    width: 170px; height: 140px; border-radius: 24px;
    background: var(--grey-mark); opacity: .75;
  }
  .front__brand {
    position: absolute; left: 36px; top: 128px;
    display: flex; align-items: flex-start; gap: 12px;
  }
  .front__brand-square {
    width: 56px; height: 56px; border-radius: 10px; background: var(--navy);
    margin-top: 4px;
  }
  .front__wordmark { display: flex; flex-direction: column; align-items: flex-end; }
  .front__brand-name {
    font-size: 50px; font-weight: 400; letter-spacing: -1.2px;
    color: var(--grey-text); line-height: 1.1;
  }
  .front__tagline {
    font-size: 15px; color: var(--navy); font-weight: 400; margin-top: -2px;
  }
  .front__person { position: absolute; left: 104px; top: 222px; }
  .front__name { font-size: 19px; font-weight: 700; color: var(--name-blue); }
  .front__title { font-size: 15px; color: var(--grey-text); margin-top: -2px; }
  .front__contacts {
    position: absolute; left: 104px; top: 280px; list-style: none;
    font-size: 14px; color: var(--name-blue); line-height: 21px;
  }
  .front__contacts li { display: flex; align-items: center; gap: 7px; }
  .contact-icon { width: 14px; height: 14px; display: block; }
  .front__band {
    position: absolute; left: 0; right: 0; bottom: 0; height: 44px;
    background: linear-gradient(90deg, var(--cyan) 0%, var(--blue-light) 35%, var(--blue) 100%);
    display: flex; align-items: center; justify-content: flex-end;
    padding-right: 28px;
  }
  .front__address { color: var(--white); font-size: 17px; font-weight: 600; letter-spacing: .3px; }

  /* back */
  .card--back {
    top: 540px;
    background: linear-gradient(160deg, var(--blue-light) 0%, var(--blue) 45%, var(--blue-deep) 100%);
  }
  .back__brand {
    position: absolute; left: 70px; top: 146px;
    display: flex; align-items: flex-start; gap: 14px;
  }
  .back__brand-square {
    width: 70px; height: 70px; border-radius: 11px; background: var(--white);
    margin-top: 4px;
  }
  .back__wordmark { display: flex; flex-direction: column; align-items: flex-end; }
  .back__brand-name {
    font-size: 64px; font-weight: 400; letter-spacing: -1.5px;
    color: var(--white); line-height: 1.1;
  }
  .back__tagline { font-size: 16px; color: var(--white); margin-top: -2px; }
  .back__social {
    position: absolute; left: 70px; top: 300px; display: flex; gap: 6px;
  }
  .back__social span {
    width: 18px; height: 18px; border-radius: 3px; background: var(--white); display: block;
  }
</style>
</head>
<body>
<main class="sheet">

  <section class="card card--front" aria-label="Business card front">
    <div class="front__mark-bg"></div>
    <div class="front__brand">
      <span class="front__brand-square"></span>
      <div class="front__wordmark">
        <span class="front__brand-name">brindleadvisory</span>
        <p class="front__tagline">business consulting</p>
      </div>
    </div>

    <div class="front__person">
      <p class="front__name">Mara Ellison</p>
      <p class="front__title">President</p>
    </div>

    <ul class="front__contacts">
      <li>
        <svg class="contact-icon" viewBox="0 0 14 14"><rect width="14" height="14" rx="3" fill="#8f949b"/><path d="M4 3.5c0 4 2.5 6.5 6.5 7l1-1.8-2-1-.9.9C7.5 8 6 6.5 5.4 5.4l.9-.9-1-2z" fill="#fff"/></svg>
        555-014-2298
      </li>
      <li>
        <svg class="contact-icon" viewBox="0 0 14 14"><rect width="14" height="14" rx="3" fill="#8f949b"/><rect x="3" y="4.5" width="8" height="5.5" fill="none" stroke="#fff" stroke-width="1"/><path d="M3 4.5l4 3 4-3" fill="none" stroke="#fff" stroke-width="1"/></svg>
        hello@brindle.com
      </li>
      <li>
        <svg class="contact-icon" viewBox="0 0 14 14"><rect width="14" height="14" rx="3" fill="#8f949b"/><circle cx="7" cy="7" r="3.6" fill="none" stroke="#fff" stroke-width="1"/><path d="M3.4 7h7.2M7 3.4v7.2" stroke="#fff" stroke-width=".8"/></svg>
        www.brindleadvisory.com
      </li>
    </ul>

    <div class="front__band">
      <p class="front__address">0000 Larch Lane Avondale, WI 00000-0000</p>
    </div>
  </section>

  <section class="card card--back" aria-label="Business card back">
    <div class="back__brand">
      <span class="back__brand-square"></span>
      <div class="back__wordmark">
        <span class="back__brand-name">brindleadvisory</span>
        <p class="back__tagline">business consulting</p>
      </div>
    </div>
    <div class="back__social" aria-label="Social profiles">
      <span></span><span></span><span></span>
    </div>
  </section>

</main>
</body>
</html>
```